Brannigan Ashcroft LLC. custom built/handcrafted

I am recent small business owner looking to sell my art(drawings) and woodworking projects from my home. I have a very rough draft of a simple card design created on a simple digital program. I was hoping for a fancier lettering on the initial letters (BA). More of a calligraphy style. Also, the yellow border around the logo I would like to be a gold foil look. For it to be shiny or reflective look and to keep the other letters black with a consistent font on the card and the card white.

Target Market(s)

Local and neighboring cities

Industry/Entity Type

Art (drawing)/Woodworking

Contact Information for Business Card

My email tpashcroft@mailvane.net, phone number 949-517-3068. In the files provided it has a yellow border around the logo and I was looking to make that a gold foil.

Font styles to use
Serif
Decorative
Script

Requirements
Nice to have
• symbols for having a Facebook and Instagram

```html
<!DOCTYPE html>
<html lang="en">
<head>
<meta charset="utf-8">
<title>Brannigan Ashcroft LLC. – Business Card</title>
<link rel="stylesheet" href="https://fonts.googleapis.com/css2?family=Merriweather:wght@300;400&display=swap">
<style>
  :root {
    --page: #ffffff;
    --card-white: #ffffff;
    --ink: #111111;
    --ink-soft: #333333;
    --gold: #f5b731;
    --gold-light: #fbd47a;
    --foil-dark: #8a6535;
    --foil-mid: #c9a06a;
    --foil-light: #ecd3a4;
  }
  * { margin: 0; padding: 0; box-sizing: border-box; }
  html, body { width: 1200px; height: 360px; overflow: hidden; background: var(--page); }
  body { position: relative; font-family: "Merriweather", Georgia, serif; color: var(--ink); }

  .card { position: absolute; top: 16px; width: 573px; height: 327px; }
  .card--front { left: 18px; }
  .card--back { left: 609px; }

  .card__foil {
    position: absolute; inset: 0;
    background:
      linear-gradient(135deg, var(--foil-light) 0%, var(--foil-mid) 22%, var(--foil-dark) 40%, var(--foil-light) 55%, var(--foil-mid) 72%, var(--foil-dark) 88%, var(--foil-light) 100%);
  }
  .card__panel {
    position: absolute; left: 31px; top: 24px; width: 511px; height: 278px;
    background: var(--card-white);
  }
  .card__frame {
    position: absolute; inset: 4px;
    border: 2px solid var(--gold);
  }

  .brand-name {
    position: absolute; white-space: nowrap;
    font-weight: 400; color: var(--ink); letter-spacing: 0.04em; text-transform: uppercase;
    transform: translateX(-50%);
  }
  .card--front .brand-name { left: 255px; top: 100px; font-size: 22px; }
  .tagline {
    position: absolute; left: 0; right: 0; top: 228px; text-align: center;
    font-size: 11.5px; color: var(--ink-soft); letter-spacing: 0.02em;
  }
  .tagline__dot { display: inline-block; margin: 0 10px; }

  .card--back .brand-name { left: 104px; top: 129px; font-size: 11px; }
  .divider {
    position: absolute; left: 208px; top: 43px; width: 2px; height: 193px;
    background: var(--gold);
  }
  .contact { position: absolute; left: 243px; top: 54px; }
  .contact__name { font-size: 17.5px; font-weight: 400; letter-spacing: 0.01em; color: #222; }
  .contact__role { margin-top: 8px; font-size: 13px; font-weight: 300; color: #444; }
  .contact__line { display: flex; align-items: center; gap: 12px; font-size: 14px; color: #222; }
  .contact__line--phone { margin-top: 22px; }
  .contact__line--email { margin-top: 14px; }
  .contact__icon { width: 16px; height: 14px; flex: none; }
  .social { display: flex; gap: 8px; margin-top: 20px; }
  .social__tile {
    width: 20px; height: 20px; border-radius: 5px;
    background: linear-gradient(180deg, var(--gold-light), var(--gold));
  }
</style>
</head>
<body>

<section class="card card--front">
  <div class="card__foil" role="img" aria-label="Faceted gold foil pattern border"></div>
  <div class="card__panel">
    <div class="card__frame"></div>
    <p class="brand-name">Brannigan Ashcroft</p>
    <p class="tagline">CUSTOM BUILT<span class="tagline__dot">•</span>HANDCRAFTED</p>
  </div>
</section>

<section class="card card--back">
  <div class="card__foil" role="img" aria-label="Faceted gold foil pattern border"></div>
  <div class="card__panel">
    <div class="card__frame"></div>
    <p class="brand-name">Brannigan Ashcroft</p>
    <div class="divider"></div>
    <div class="contact">
      <h1 class="contact__name">THOMAS P. ASHCROFT</h1>
      <p class="contact__role">Owner</p>
      <p class="contact__line contact__line--phone">
        <svg class="contact__icon" viewBox="0 0 16 16" aria-hidden="true">
          <path fill="#f5b731" d="M3.2 1.2l2.4 0 1.2 3.3-1.6 1.2c.8 1.9 2.3 3.4 4.2 4.2l1.2-1.6 3.3 1.2v2.4c0 .9-.8 1.7-1.7 1.6C6.4 13 2.9 9.6 2 4.4c-.1-.9.6-1.7 1.2-1.7z"/>
        </svg>
        949-517-3068
      </p>
      <p class="contact__line contact__line--email">
        <svg class="contact__icon" viewBox="0 0 16 12" aria-hidden="true">
          <rect x="0" y="0" width="16" height="12" fill="#f5b731"/>
          <path d="M0 0 L8 7 L16 0" fill="none" stroke="#fff" stroke-width="1.3"/>
          <path d="M0 12 L6 6 M16 12 L10 6" stroke="#fff" stroke-width="1"/>
        </svg>
        tpashcroft@mailvane.net
      </p>
      <div class="social" aria-label="Social media">
        <span class="social__tile"></span>
        <span class="social__tile"></span>
      </div>
    </div>
  </div>
</section>

</body>
</html>
```